Awesome Flyer for Tactical Emergency Response Services

We need a Flyer for Emergency Rapid Response services for my company ferncrest Security Services Ltd. , we are a security guisard service based in Trinidad in the Caribbean.
The flyer will include price and pictures of our tactical team. must be clear concise, and strong.

Rapid response services is where customers pay a monthly fee and if they have any security issues they call us and we immediately respond to their home or business to ensure their safety and security.

Target Market(s)

Homeowners; people worried about home security such as home invasions etc.

Requirements
Must have
• Company Logo prominent

```html
<!DOCTYPE html>
<html lang="en">
<head>
<meta charset="utf-8">
<title>Ferncrest Security Services – 24 HR Emergency Rapid Response</title>
<link rel="stylesheet" href="https://fonts.googleapis.com/css2?family=Montserrat:wght@500;600;700;800&family=Oswald:wght@600;700&display=swap">
<style>
  :root {
    --brand-red: #e11d2a;
    --ink: #111111;
    --paper: #ffffff;
    --stage: #e8e5e1;
    --photo-green: #4f6a3a;
    --photo-grey: #8c8a84;
  }
  * { box-sizing: border-box; margin: 0; padding: 0; }
  html, body { width: 1200px; height: 1200px; overflow: hidden; }
  body {
    background: var(--stage);
    font-family: "Montserrat", sans-serif;
    color: var(--ink);
  }
  .flyer {
    position: absolute;
    left: 175px; top: 0;
    width: 850px; height: 1200px;
    background: var(--paper);
    overflow: hidden;
  }
  .hero-photo {
    position: absolute; left: 0; top: 0;
    width: 850px; height: 460px;
    background: linear-gradient(180deg, #9fb07e 0%, var(--photo-grey) 35%, #5a5550 60%, var(--photo-green) 100%);
  }
  .shapes { position: absolute; left: 0; top: 0; width: 850px; height: 1200px; }
  .headline {
    position: absolute; left: 40px; top: 470px; width: 540px;
    text-align: center;
    color: var(--paper);
    font-weight: 800; font-size: 46px; line-height: 1.12;
    letter-spacing: 1px;
    white-space: nowrap;
  }
  .team-photo { position: absolute; border-radius: 50%; }
  .team-photo--drill {
    left: 580px; top: 545px; width: 230px; height: 230px;
    background: radial-gradient(circle at 40% 40%, #b9b6ae, #6b6a63 60%, #4d5e36);
    box-shadow: 0 0 0 6px var(--paper), 0 0 0 15px var(--ink);
  }
  .team-photo--vehicle {
    left: 545px; top: 790px; width: 170px; height: 170px;
    background: radial-gradient(circle at 50% 60%, #2a2a2a, #5e6a4a 55%, #9aa48c);
    box-shadow: 0 0 0 5px var(--paper), 0 0 0 12px var(--brand-red);
  }
  .benefits {
    position: absolute; left: 70px; top: 745px; width: 440px;
    list-style: none;
    font-weight: 500; font-size: 17px; line-height: 1.3;
  }
  .benefits li {
    display: flex; align-items: flex-start; gap: 14px;
    margin-bottom: 9px;
  }
  .benefits svg { flex: 0 0 22px; margin-top: 1px; }
  .price-card {
    position: absolute; left: 60px; top: 880px; width: 460px; height: 120px;
    border-radius: 40px;
    background: linear-gradient(135deg, #000 0%, #2b2b2b 100%);
    color: var(--paper);
    text-align: center;
    padding-top: 14px;
  }
  .price-card__amount {
    font-family: "Oswald", sans-serif;
    font-weight: 700; font-size: 42px; line-height: 1.1;
  }
  .price-card__offer { font-weight: 500; font-size: 17px; line-height: 1.3; }
  .brand {
    position: absolute; left: 585px; top: 985px;
    display: flex; align-items: center; gap: 12px;
  }
  .brand__mark {
    width: 44px; height: 44px; border-radius: 50%;
    background: var(--brand-red);
  }
  .brand__name {
    color: var(--brand-red);
    font-weight: 700; font-size: 17px; line-height: 1.2;
  }
  .contact {
    position: absolute; left: 70px; top: 1012px;
    font-style: normal;
    font-weight: 600; font-size: 25px; line-height: 1.3;
  }
  .contact__title { color: var(--brand-red); font-weight: 800; }
</style>
</head>
<body>
  <main class="flyer">
    <div class="hero-photo" role="img" aria-label="Photo of the tactical response team standing in front of branded patrol cars"></div>

    <svg class="shapes" viewBox="0 0 850 1200" aria-hidden="true">
      <path d="M0 440 Q425 400 850 320 L850 1200 L0 1200 Z" fill="#ffffff"/>
      <path d="M0 440 Q425 400 850 320" fill="none" stroke="#111111" stroke-width="8"/>
      <path d="M0 454 Q425 414 850 334 L850 580 Q425 640 0 710 Z" fill="var(--brand-red)"/>
      <path d="M0 722 Q425 652 850 592" fill="none" stroke="#111111" stroke-width="5"/>
      <path d="M0 1200 L850 1100 L850 1200 Z" fill="var(--brand-red)"/>
    </svg>

    <h1 class="headline">24 HR EMERGENCY<br>RAPID RESPONSE</h1>

    <div class="team-photo team-photo--drill" role="img" aria-label="Photo of officers in a tactical formation against a wall"></div>
    <div class="team-photo team-photo--vehicle" role="img" aria-label="Photo of a vehicle stop training drill"></div>

    <ul class="benefits">
      <li>
        <svg width="22" height="22" viewBox="0 0 22 22"><circle cx="11" cy="11" r="10" fill="var(--brand-red)"/><path d="M6 11.5l3.2 3.2L16 8" fill="none" stroke="#fff" stroke-width="2.4"/></svg>
        <span>Fully equipped and specially trained in tactical rapid response protocols</span>
      </li>
      <li>
        <svg width="22" height="22" viewBox="0 0 22 22"><circle cx="11" cy="11" r="10" fill="var(--brand-red)"/><path d="M6 11.5l3.2 3.2L16 8" fill="none" stroke="#fff" stroke-width="2.4"/></svg>
        <span>Protecting you 24/7</span>
      </li>
      <li>
        <svg width="22" height="22" viewBox="0 0 22 22"><circle cx="11" cy="11" r="10" fill="var(--brand-red)"/><path d="M6 11.5l3.2 3.2L16 8" fill="none" stroke="#fff" stroke-width="2.4"/></svg>
        <span>Delivering Peace of mind to our clients</span>
      </li>
    </ul>

    <section class="price-card">
      <p class="price-card__amount">$200 + VAT PER MONTH</p>
      <p class="price-card__offer">Sign up for 12 months and receive a<br>10% discount</p>
    </section>

    <div class="brand">
      <span class="brand__mark"></span>
      <p class="brand__name">FERNCREST<br>SECURITY SERVICES</p>
    </div>

    <address class="contact">
      <p class="contact__title">Contact</p>
      <p>Tel : 555-0148 &nbsp;| 555-0172</p>
      <p>Email : info@ferncrest-tt.com</p>
    </address>
  </main>
</body>
</html>
```